" Trabalho de forma autônoma como Coach Executivo. O Coaching executivo pode ser contratado tanto por PJ como por PF. São sessões / reuniões nas quais trabalhamos de forma individual para desenvolvimento da pessoa - desenvolvimento de habilidades, autoconsciência dos pontos fortes e pontos a serem desenvolvidos, para que a pessoa desempenhe seu máximo em sua carreira profissional e atinja o sucesso que ela determinou. O foco do trabalho é o desenvolvimento de competências / habilidades para ela desempenhar seu trabalho e se desenvolver em sua carreira profissional com excelência. Também tem o foco, no Coaching de Carreira, na redefinição dos rumos profissionais de uma pessoa. Discussão de possibilidades de caminhos a serem seguidos e uma reflexão do que aconteceu até o momento. Em ambos os casos, é um processo de autoreflexão mas que já parte para a AÇÃO. Não tem nada de estático, só ficar pensando e divagando em ideias. O ponto é fazer com que a pessoa se mova, saia do lugar, vá buscar seus objetivos. Esse apoio durante o processo também é dado para que a ação efetivamente aconteça. "

```html
<!DOCTYPE html>
<html lang="pt-BR">
<head>
<meta charset="UTF-8">
<title>Marina Tavares Coaching – Papel Timbrado</title>
<link rel="stylesheet" href="https://fonts.googleapis.com/css2?family=Cinzel:wght@400&family=Arimo:wght@400&display=swap">
<style>
  :root {
    --backdrop: #1b1e1d;
    --paper: #ffffff;
    --ink: #2f3433;
    --accent: #4fb3c6;
    --muted: #555b5a;
  }
  html, body {
    margin: 0;
    width: 1200px;
    height: 1200px;
    overflow: hidden;
    background: var(--backdrop);
  }
  .letterhead {
    position: absolute;
    left: 312px;
    top: 240px;
    width: 576px;
    height: 756px;
    background: var(--paper);
    box-shadow: 0 2px 10px rgba(0,0,0,0.35);
  }
  .brand {
    position: absolute;
    top: 60px;
    left: 0;
    width: 100%;
    text-align: center;
  }
  .brand-dot {
    display: block;
    width: 30px;
    height: 30px;
    margin: 0 auto 8px;
    border-radius: 50%;
    background: var(--accent);
  }
  .brand-name {
    margin: 0;
    font-family: "Cinzel", serif;
    font-weight: 400;
    font-size: 29px;
    letter-spacing: 1px;
    color: var(--ink);
    line-height: 1.1;
  }
  .brand-tagline {
    margin: 2px 0 0 88px;
    font-family: "Cinzel", serif;
    font-size: 8px;
    letter-spacing: 6px;
    color: var(--ink);
    text-transform: uppercase;
    text-align: center;
  }
  .contact {
    position: absolute;
    top: 680px;
    left: 0;
    width: 100%;
    text-align: center;
    font-family: "Arimo", Arial, sans-serif;
    font-size: 17px;
    line-height: 25px;
    color: var(--muted);
  }
  .contact p { margin: 0; }
</style>
</head>
<body>
  <main class="letterhead">
    <header class="brand">
      <span class="brand-dot" aria-hidden="true"></span>
      <h1 class="brand-name">Marina Tavares</h1>
      <p class="brand-tagline">Coaching</p>
    </header>
    <footer class="contact">
      <p>tel. 11 90000-1234</p>
      <p>Email: ma.tavares@exemplo.com.br</p>
      <p>Perfil: br.perfilpro.com/in/marina-tavares</p>
    </footer>
  </main>
</body>
</html>
```